Digital Imaging Website Design Project

This project is for 3 page designs - The main Home page design, department page design & content page design which will utilize most of the home page components.

Client Background - http://www.kelrofab.com

An almost Forty year old established printing company that has a large client base of architect/engineering, as the print shop opened up as a blueprinting company, and over the years has grown, changed and expanded to offer document and digital file management for this industry. KRFab. has also always offered color printing services, but recently has expanded their color department to be able to offer amazing dimensional printing, and extreme cutting technology.

These new products and services will be targeted to new industries for repeatable printing needs, promotional, point of purchase color printing, as well as in-store, interior decor/wall. These new printing services are only offered by KRFAB in their area, and they want to convey that they are on the leading edge of color printing technology, while at the same time, not eliminating their existing primary business scaring away their traditional client base of architectural/engineering firms that use them for large format printing, scanning and document management services.

1 - Home Page Design
Primary Goals of the design:

1.Provide a new, eye catching engaging website that conveys the above expansion/growth/cutting edge company.
2.Full screen design please to move away from the 'center' bordered up website they currently have.
3.Design Components – We don't have any media to provide you with exception of our logo. We're looking for fresh design that is exciting and engaging imagery. Additionally, we are working on a color/effected version of our logo to place on the color division page, and this will probably tie in with the design you create for us.
4.It should be designed to be able to work as a responsive design as well so that when installed, will work across devices etc..
5.Colors – Same color scheme, but if you have an accent color you'd like to use to make the site pop, go for it!

Requirements:
1.The 4 divisions of the company should be the main feature so that the client depending on which department they are needing, will see those 4 choices clearly in the design, and they'll know to click on one of them to get more information and to their needed services.

2.The main goal of the site is to get visitors to place an order, there should be a feature on the home page for this call to action.

3.Put in an element that communicates the main benefit of KRFab. - an area for a 1-line Statement/Call to Action / Overall Company Benefit/

4.The 4 divisions need to have eye catching elements related to their products and services, and that clearly illustrate that the user should click on that to go to the appropriate area for products and services

Reprographics
This department is specifically geared to architect/engineering industry
BYLine for optional Use: Partnering with Building Industry Providers since 1975
Related pages for better understanding:
http://www.kelrofab.com/services/portland_professional_printing_services
http://www.kelrofab.com/services/reprographics
Digital File Management
This department is related to Architect/engineers, but can also apply to any other industry needing electronic document management, scanning, or archival services.
BYLine for optional use: Effective & Efficient Digital Solutions at every level.
Related Pages:
http://www.kelrofab.com/colorgraphics/electronic_file_document_management
http://www.kelrofab.com/colorgraphics/document_scanning_service
http://www.kelrofab.com/services/scanning_and_archiving

Color Graphics
This Department is newly expanded / has expanded services / they are focusing more of their efforts on this department and is a key reason for updated website design.
This Department image/representation should be stellar in the imagery to convey the excellence of the color department the services availble.
One of their newest products/services is dimensional printing – not 3-D, but raised element printing. Essentially a client could pick components on their graphic that that they want to 'bump' out, and additional layers would be put in place to create a popped out, dimensional effect. * Bonus points for creating the color department image that effectively conveys this new service – whether it's showing an abstract image/element that is actually raised off the page/paper/component. Additionally the color dimensional printing can be done on practically any material – glass, vinyl, material etc.... Please let me know if you have any questions on this.
BYLine for optional Use: See How Our Color Stands Out From the Rest
Related pages:
http://www.kelrofab.com/colorgraphics
http://www.kelrofab.com/colorgraphics/color_digital_imaging

Equipment & Supplies
This department provides specific supplies and hardware vs. printing products/services. Our largest client base is architects/engineers, but is not limited to this industry. Typical equipment is large printers, and supplies are typically paper products geared to the large format printing services, for the architect/engineers industry.
Byline for optional Use: In-House Printing & Fulfillment Services
Related pages:
http://www.kelrofab.com/varlen_tusk_equipment_sales
http://www.kelrofab.com/supplies

Additionally - Possibly have descriptive text sections below these 4 elements, but this is optional.

2.) Department/Division Page design -

This page should pull the home page element to over based on which division is selected.
Have a submenu design incorporated so that users can navigate to all the products and services that will be listed under that division
Contain a plugin design for FAQs – so that depending on which division page they are on, the appropriate FAQ's would display for use to have easy access to.
Contain a plugin design for – Contact Us easy form – short form –
Name
Company
Number
Email
Project Details/Questions: Text box

3.)Content Page design
This page should have main area for content
Area for an image with slideshow of other supporting images
Optional area for video – most (99%) of the pages will not have videos, but in the case we do, would like an area that will display videos effectively.
Optional FAQ plugin display
Contact plugin display

Global Elements:

Static and very visible site features that are in a position so that if user clicks beyond home page will still see these are:
Get a Quote
Place Order
Digital Plan-room
Call Today - 503-481-7962

Other global components:
SM Icons – QN, Chirpo, WorkLoop
Rotating Testimonial

Navigational Menu:
The KRF Difference
About
Sustainability
Products & Services
Reprograhics
Digital File Management
Color Graphics
Equipment & Supplies
Login
Blog
Contact Us

After the contest – What would be great to have is when a user clicks on one of the departments, it takes that visual element and continues onto it's department page for a smaller but related image - But this may be an after this web design contest.

Additionally will need some other design work on the interior pages, as well, so hoping to find a great designer to complete the other tasks – as well as be the go-to for future endeavors!

Thanks for looking at the project, and I look forward to any questions you may have.
Updates

Looking forward to hearing from interested designers! - If you're curious about my work, you can find my profile at:  https://www.gigmarla.com/users/~07b3e2f95d18c4a260

Target Market(s)

Please see description

Industry/Entity Type

Electronic

Requirements
Must have
• Please see description

```html
<!DOCTYPE html>
<html lang="en">
<head>
<meta charset="utf-8">
<title>Kelro Print &amp; Fabrication – Home</title>
<link href="https://fonts.googleapis.com/css2?family=Figtree:wght@400;500;600;700;800&display=swap" rel="stylesheet">
<style>
  :root{
    --navy:#141b85;
    --band-1:#141b85;
    --band-2:#161f96;
    --band-3:#1c28c3;
    --band-4:#2835d9;
    --phone-blue:#2a63b8;
    --green:#8cc21f;
    --grey-text:#5d5d5d;
    --grey-light:#c8c8c8;
    --dots:#cfcfcf;
    --white:#ffffff;
  }
  *{box-sizing:border-box;margin:0;padding:0}
  html,body{width:1200px;height:882px;overflow:hidden;background:var(--white)}
  body{font-family:"Figtree",Arial,sans-serif;color:var(--grey-text);position:relative}
  a{color:inherit;text-decoration:none}

  .edge-bar{position:absolute;left:0;width:1200px;height:8px;background:var(--grey-light)}
  .edge-bar.top{top:0}
  .edge-bar.bottom{bottom:0}

  /* header */
  .brand{position:absolute;left:150px;top:38px;display:flex;align-items:flex-start;gap:12px;color:var(--navy)}
  .brand-mark{width:62px;height:62px;background:var(--navy);flex:none}
  .brand-name{font-weight:700;font-size:15.5px;line-height:17px;text-transform:uppercase;width:150px;letter-spacing:.2px}
  .brand-tagline{position:absolute;left:74px;top:60px;font-size:10.5px;font-weight:700;white-space:nowrap}

  .social{position:absolute;top:32px;left:754px;display:flex;gap:8px}
  .social a{width:20px;height:20px;border-radius:50%;background:#555;display:block}

  .utility{position:absolute;top:37px;right:146px;font-size:11.5px;color:var(--grey-text);letter-spacing:.2px}

  .call{position:absolute;top:73px;right:146px;display:flex;align-items:flex-end;gap:8px}
  .call svg{width:24px;height:32px;margin-bottom:1px}
  .call-label{font-size:11.5px;font-weight:700;color:var(--grey-text);letter-spacing:.2px;line-height:1}
  .call-number{font-size:29px;font-weight:800;color:var(--phone-blue);letter-spacing:-1px;line-height:1;margin-top:2px}

  .main-nav{position:absolute;top:163px;left:150px;width:905px;display:flex;justify-content:space-between;font-size:10.6px;color:var(--navy);text-transform:uppercase;letter-spacing:.1px}

  /* divisions */
  .divisions{position:absolute;top:198px;left:0;width:1200px}
  .division{height:100.75px;display:flex;align-items:center;position:relative;color:var(--white)}
  .division:nth-child(1){background:var(--band-1)}
  .division:nth-child(2){background:var(--band-2)}
  .division:nth-child(3){background:var(--band-3)}
  .division:nth-child(4){background:var(--band-4)}
  .division-art{position:absolute;left:152px;width:84px;height:76px;border-radius:6px}
  .art-hat{background:linear-gradient(180deg,#f3d542,#d2a814)}
  .art-cabinet{background:linear-gradient(180deg,#e6e6e6,#a9a9a9)}
  .art-color{background:linear-gradient(135deg,#d94848,#6fa84a 55%,#4a7ac8)}
  .art-paint{background:linear-gradient(180deg,#d6dee8,#8f9fb3)}
  .division-title{position:absolute;left:252px;font-size:23px;font-weight:800;letter-spacing:-1px;text-transform:uppercase;white-space:nowrap}
  .division-byline{position:absolute;font-size:11.6px;font-weight:500;letter-spacing:.2px;margin-top:4px;white-space:nowrap}
  .chevron{position:absolute;left:1030px;width:28px;height:44px}

  /* benefit */
  .benefit{position:absolute;top:617px;left:161px;font-size:12.2px;font-weight:700;text-transform:uppercase;color:var(--grey-text);letter-spacing:.1px;white-space:nowrap}
  .rule{position:absolute;left:158px;width:890px;border-top:1px dotted var(--dots)}

  .actions{position:absolute;top:665px;left:158px;height:98px;display:flex}
  .action{position:relative;height:98px}
  .action + .action{border-left:1px dotted var(--dots)}
  .action svg{position:absolute;top:0}
  .action h3{position:absolute;top:30px;font-size:15.7px;font-weight:800;color:var(--navy);text-transform:uppercase;letter-spacing:-.7px;white-space:nowrap}
  .action p{position:absolute;top:50px;font-size:9.2px;line-height:12px;color:var(--grey-text);width:130px}
  .action .more{position:absolute;top:80px;font-size:10.5px;font-weight:700;color:var(--green)}

  .testimonials h2{position:absolute;top:-3px;left:20px;font-size:22.5px;font-weight:800;color:var(--navy);letter-spacing:-1px;text-transform:uppercase}
  .testimonials blockquote{position:absolute;top:37px;left:25px;width:292px;font-size:9.4px;line-height:12px;color:var(--grey-text)}
  .testimonials cite{position:absolute;top:80px;left:25px;font-style:normal;font-size:10.5px;font-weight:700;color:var(--green);white-space:nowrap}

  /* footer */
  .site-footer{position:absolute;top:808px;left:161px;font-size:11px;line-height:18px}
  .footer-contact{color:var(--navy);display:flex;gap:15px}
  .footer-copy{color:var(--grey-text)}
  .footer-brand{position:absolute;top:808px;right:150px;display:flex;align-items:center;gap:5px;color:#c4c4c4;font-weight:800;font-size:20px;letter-spacing:-.5px}
  .footer-brand span.box{width:16px;height:16px;background:#d4d4d4}
</style>
</head>
<body>
  <div class="edge-bar top"></div>

  <header class="site-header">
    <a class="brand" href="#">
      <span class="brand-mark" aria-hidden="true"></span>
      <span class="brand-name">Kelro Print &amp; Fabrication Company, Inc.</span>
      <span class="brand-tagline">Client-Driven Service Since 1975</span>
    </a>

    <nav class="social" aria-label="Social">
      <a href="#" aria-label="QN"></a>
      <a href="#" aria-label="WorkLoop"></a>
      <a href="#" aria-label="Chirpo"></a>
    </nav>

    <div class="utility"><a href="#">LOGIN</a> &nbsp;- <a href="#">BLOG</a> - <a href="#">CONTACT US</a></div>

    <div class="call">
      <svg viewBox="0 0 26 34" aria-hidden="true"><path d="M6 2c2-1 4 0 5 2l2 6c0 2-1 3-3 4 1 4 3 7 6 9 1-2 3-3 5-2l3 4c1 2 0 4-2 5-3 2-8 1-12-4C5 21 2 14 2 9c0-3 2-6 4-7z" fill="var(--green)"/></svg>
      <div>
        <div class="call-label">CALL US TODAY</div>
        <div class="call-number">503-481-7962</div>
      </div>
    </div>

    <nav class="main-nav" aria-label="Main">
      <a href="#">The KRF Difference</a>
      <a href="#">About</a>
      <a href="#">Sustainability</a>
      <a href="#">Products &amp; Services</a>
      <a href="#">Reprographics</a>
      <a href="#">Digital File Management</a>
      <a href="#">Color Graphics</a>
      <a href="#">Equipment &amp; Supplies</a>
    </nav>
  </header>

  <main>
    <section class="divisions">
      <a class="division" href="#">
        <div class="division-art art-hat" role="img" aria-label="Illustration of a yellow construction hard hat"></div>
        <span class="division-title">Reprographics</span>
        <span class="division-byline" style="left:457px">Partnering with Building Industry Providers since 1975</span>
        <svg class="chevron" viewBox="0 0 28 44" aria-hidden="true"><path d="M4 3l19 19L4 41" fill="none" stroke="#3344c8" stroke-width="5"/></svg>
      </a>
      <a class="division" href="#">
        <div class="division-art art-cabinet" role="img" aria-label="Illustration of a silver filing cabinet with an open drawer"></div>
        <span class="division-title">Digital File Management</span>
        <span class="division-byline" style="left:557px">Effective &amp; Efficient Digital Solutions at every level.</span>
        <svg class="chevron" viewBox="0 0 28 44" aria-hidden="true"><path d="M4 3l19 19L4 41" fill="none" stroke="#3443cc" stroke-width="5"/></svg>
      </a>
      <a class="division" href="#">
        <div class="division-art art-color" role="img" aria-label="Illustration of a colour dial with a paintbrush"></div>
        <span class="division-title">Color Graphics</span>
        <span class="division-byline" style="left:460px">See How Our Color Stands Out From the Rest</span>
        <svg class="chevron" viewBox="0 0 28 44" aria-hidden="true"><path d="M4 3l19 19L4 41" fill="none" stroke="#3a49dd" stroke-width="5"/></svg>
      </a>
      <a class="division" href="#">
        <div class="division-art art-paint" role="img" aria-label="Illustration of a paint can with a brush"></div>
        <span class="division-title">Equipment &amp; Supplies</span>
        <span class="division-byline" style="left:524px">In-House Printing &amp; Fulfillment Services</span>
        <svg class="chevron" viewBox="0 0 28 44" aria-hidden="true"><path d="M4 3l19 19L4 41" fill="none" stroke="#4655e6" stroke-width="5"/></svg>
      </a>
    </section>

    <p class="benefit">We utilize the latest digital technologies to provide a wide range of reprographics and graphic imaging services.</p>
    <div class="rule" style="top:647px"></div>

    <section class="actions">
      <div class="action" style="width:155px">
        <svg style="left:38px" width="22" height="22" viewBox="0 0 22 22" aria-hidden="true"><rect x="5" y="1" width="16" height="12" rx="2" fill="var(--navy)"/><path d="M1 7h3v7h8v4H6l-3 3v-3H1z" fill="var(--navy)"/></svg>
        <h3 style="left:4px">Get a Quote</h3>
        <p style="left:2px">Lorem ipsum dolor sit amet, consectetuer ...</p>
        <a class="more" style="left:1px" href="#">Read More...</a>
      </div>
      <div class="action" style="width:174px">
        <svg style="left:78px" width="22" height="22" viewBox="0 0 22 22" aria-hidden="true"><path d="M7 7l3-6M15 7l-3-6" stroke="var(--navy)" stroke-width="1.6" fill="none"/><rect x="2" y="7" width="18" height="3" fill="var(--navy)"/><path d="M3 11h16l-2 10H5z" fill="var(--navy)"/><path d="M7 13v6M11 13v6M15 13v6" stroke="#fff" stroke-width="1"/></svg>
        <h3 style="left:26px">Place Order</h3>
        <p style="left:27px">Lorem ipsum dolor sit amet, consectetuer ...</p>
        <a class="more" style="left:26px" href="#">Read More...</a>
      </div>
      <div class="action" style="width:198px">
        <svg style="left:87px" width="22" height="22" viewBox="0 0 22 22" aria-hidden="true"><circle cx="11" cy="11" r="10" fill="none" stroke="var(--navy)" stroke-width="2"/><path d="M1 11h20M11 1c-4 4-4 16 0 20M11 1c4 4 4 16 0 20" fill="none" stroke="var(--navy)" stroke-width="1.4"/></svg>
        <h3 style="left:26px">Digital Plan-Room</h3>
        <p style="left:26px">Lorem ipsum dolor sit amet, consectetuer ...</p>
        <a class="more" style="left:26px" href="#">Read More...</a>
      </div>
      <div class="action testimonials" style="width:360px">
        <h2>Testimonials</h2>
        <blockquote>Lorem ipsum dolor sit amet, consectetuer adipiscing elit, sed diam nonummy nibh euismod tincidunt ut laoreet dolore magna aliquam erat volutpat.</blockquote>
        <cite>Dale Mercer, Principle</cite>
      </div>
    </section>

    <div class="rule" style="top:790px"></div>
  </main>

  <footer>
    <div class="site-footer">
      <div class="footer-contact"><span>Portland Office (503) 481-7962</span><span>Questions/Comments: email us at info@kelrofab.com</span></div>
      <div class="footer-copy">© Copyright 2013 Kelro Print &amp; Fabrication Inc</div>
    </div>
    <div class="footer-brand"><span class="box" aria-hidden="true"></span><span>KRF</span></div>
  </footer>

  <div class="edge-bar bottom"></div>
</body>
</html>
```